Vantro #27 - MEN'S NATURAL THERAPEUTIC INTIMATE WASH

Men's Natural Therapeutic INTIMATE Wash
VANTRO #27

Design a 4 oz. stand up tube with flip top cap...
To be packaged in a carton/box

Formula contains Tea Tree OIL
Aloe Vera Gel
Coconut Oil

PRODUCT IS A WASH/SOAP

Helps with
- Jock Itch (tinea cruris)
- Skin Rashes
- Candida
- Itchy Skin

COLORS ON TUBE: Gray, Black, Lime Electric Green and Blue

PRODUCT FOR MEN!

Target Market(s)

MEN

Industry/Entity Type

Retail

Font styles to use
Sans Serif

Colors
9bcb3b
abd036
33a6d7
000000
c9c9c9

Requirements
Must have
• Colors... black, gray, electric green and blue
Nice to have
• Needs to look masculine appeal to the male consumer

```html
<!DOCTYPE html>
<html lang="en">
<head>
<meta charset="utf-8">
<title>Vantro #27 — Men's Natural Therapeutic Intimate Wash</title>
<link rel="stylesheet" href="https://fonts.googleapis.com/css2?family=Source+Sans+3:wght@400;600;700;800&display=swap">
<style>
  :root {
    --black: #000000;
    --gray: #c9c9c9;
    --light-gray: #dcdcdc;
    --lime: #9bcb3b;
    --green: #abd036;
    --blue: #33a6d7;
    --text-dark: #111111;
    --page: #ffffff;
  }
  * { margin: 0; padding: 0; box-sizing: border-box; }
  html, body {
    width: 1056px;
    height: 1200px;
    overflow: hidden;
    background: var(--page);
    font-family: "Source Sans 3", sans-serif;
  }
  .carton-front {
    position: absolute;
    left: 238px;
    top: 10px;
    width: 580px;
    height: 1180px;
    background: var(--black);
    overflow: hidden;
  }
  .carton-shapes {
    position: absolute;
    inset: 0;
  }
  .brand {
    position: absolute;
    left: 55px;
    top: 124px;
  }
  .brand-name {
    font-size: 46px;
    font-weight: 700;
    color: var(--light-gray);
    letter-spacing: 1px;
    line-height: 1;
  }
  .product-title {
    position: absolute;
    left: 53px;
    top: 340px;
    line-height: 1;
  }
  .title-audience {
    display: block;
    font-size: 118px;
    font-weight: 800;
    color: var(--light-gray);
    letter-spacing: 1px;
  }
  .title-claim {
    display: block;
    margin-top: 14px;
    font-size: 46px;
    font-weight: 600;
    color: var(--lime);
    letter-spacing: -0.5px;
  }
  .title-type {
    display: block;
    margin-top: 18px;
    font-size: 60px;
    font-weight: 600;
    color: var(--light-gray);
  }
  .ingredients {
    position: absolute;
    left: 34px;
    top: 722px;
    list-style: none;
  }
  .ingredient {
    height: 35px;
    margin-bottom: 15px;
    background: var(--gray);
    clip-path: polygon(0 0, 100% 0, calc(100% - 22px) 100%, 0 100%);
    color: var(--black);
    font-size: 20px;
    font-weight: 700;
    display: flex;
    align-items: center;
    justify-content: center;
    padding-right: 18px;
    letter-spacing: 0.3px;
  }
  .ingredient--tea { width: 328px; }
  .ingredient--aloe { width: 287px; }
  .ingredient--coconut { width: 246px; }
  .benefits {
    position: absolute;
    right: 84px;
    top: 862px;
    text-align: right;
    list-style: none;
    color: var(--text-dark);
    font-size: 20px;
    font-weight: 600;
    line-height: 31px;
  }
  .net-weight {
    position: absolute;
    left: 0;
    right: 0;
    top: 1119px;
    height: 61px;
    display: flex;
    align-items: center;
    justify-content: center;
    font-size: 36px;
    font-weight: 800;
    color: var(--black);
  }
</style>
</head>
<body>
  <main class="carton-front">
    <svg class="carton-shapes" width="580" height="1180" viewBox="0 0 580 1180" aria-hidden="true">
      <polygon class="corner-blue" points="343,0 580,0 580,237" fill="var(--blue)"/>
      <polygon class="diagonal-green" points="580,550 580,1103 53,1103" fill="var(--green)"/>
      <rect class="stripe-gray" x="0" y="1103" width="580" height="16" fill="var(--gray)"/>
      <rect class="band-blue" x="0" y="1119" width="580" height="61" fill="var(--blue)"/>
    </svg>

    <div class="brand">
      <span class="brand-name">VANTRO #27</span>
    </div>

    <h1 class="product-title">
      <span class="title-audience">MEN'S</span>
      <span class="title-claim">NATURAL THERAPEUTIC</span>
      <span class="title-type">INTIMATE Wash</span>
    </h1>

    <ul class="ingredients">
      <li class="ingredient ingredient--tea">TEA TREE OIL</li>
      <li class="ingredient ingredient--aloe">ALOE VERA GEL</li>
      <li class="ingredient ingredient--coconut">COCONUT OIL</li>
    </ul>

    <ul class="benefits">
      <li>Helps with</li>
      <li>CANDIDA</li>
      <li>ITCHY SKIN</li>
      <li>SKIN RASHES</li>
      <li>JOCK ITCH (TINEA CRURIS)</li>
    </ul>

    <p class="net-weight">4 oz.</p>
  </main>
</body>
</html>
```